CD Cover Design Project w/ Committed Payout.

We need a CD cover design for our first release from our new christian record label.

The title of the CD is called

"The Radiant Harbor Anthology Volume 1"

This will have to tactfully go on the cover...

Perhaps the attached logo can be somewhere on the cover and "presents" and then the CD name...

Additionally - will need the back of the CD as well to co-inside with the front design. The back design will have artist and song listing as well as the 371 Records logo on the bottom, and the CD # which will be #371-1 with a place for a UPC scanner code.

Please leave the artist and song lists as "Artist 1 - Song 1", etc. for now

Target Market(s)

everyone

Industry/Entity Type

Christian

Requirements
Must have
• something with the image of the world and somehow something positively impacting it.

```html
<!DOCTYPE html>
<html lang="en">
<head>
<meta charset="utf-8">
<title>The Radiant Harbor Anthology Volume 1 – Disc Label</title>
<link rel="stylesheet" href="https://fonts.googleapis.com/css2?family=Audiowide&family=Montserrat:wght@400&display=swap">
<style>
  :root {
    --page: #ffffff;
    --disc: #000000;
    --band-deep: #0d3442;
    --band-mid: #1d6a85;
    --band-light: #3aa3c4;
    --title-fill: #ffffff;
    --title-edge: #1f8fff;
    --title-glow: #2aa0ff;
    --hub-outer: #f4f4f4;
    --hub-ring: #d2d2d2;
    --hub-inner: #fafafa;
    --label-ink: #ffffff;
  }
  html, body {
    margin: 0;
    padding: 0;
    width: 1200px;
    height: 960px;
    overflow: hidden;
    background: var(--page);
  }
  .disc-label {
    display: block;
    width: 1200px;
    height: 960px;
  }
  .disc-title {
    font-family: "Audiowide", sans-serif;
    font-size: 40px;
    fill: var(--title-fill);
    stroke: var(--title-edge);
    stroke-width: 2.5px;
    paint-order: stroke;
    letter-spacing: 0.5px;
  }
  .disc-subtitle {
    font-family: "Audiowide", sans-serif;
    font-size: 19px;
    fill: var(--title-fill);
    stroke: var(--title-edge);
    stroke-width: 1.6px;
    paint-order: stroke;
    letter-spacing: 0.5px;
  }
  .label-number {
    font-family: "Montserrat", sans-serif;
    font-weight: 400;
    font-size: 78px;
    fill: var(--label-ink);
  }
  .label-word {
    font-family: "Montserrat", sans-serif;
    font-weight: 400;
    font-size: 20px;
    fill: var(--label-ink);
    letter-spacing: 9px;
  }
</style>
</head>
<body>
<svg class="disc-label" viewBox="0 0 1200 960" xmlns="http://www.w3.org/2000/svg">
  <defs>
    <clipPath id="disc-edge">
      <circle cx="600" cy="483" r="442"/>
    </clipPath>
    <linearGradient id="band-top" x1="0" y1="0" x2="1" y2="1">
      <stop offset="0" stop-color="var(--band-deep)"/>
      <stop offset="0.5" stop-color="var(--band-light)"/>
      <stop offset="1" stop-color="var(--band-mid)"/>
    </linearGradient>
    <linearGradient id="band-bottom" x1="0" y1="0" x2="1" y2="1">
      <stop offset="0" stop-color="var(--band-mid)"/>
      <stop offset="0.5" stop-color="var(--band-light)"/>
      <stop offset="1" stop-color="var(--band-deep)"/>
    </linearGradient>
    <radialGradient id="hub-shade" cx="0.45" cy="0.4" r="0.7">
      <stop offset="0" stop-color="#ffffff"/>
      <stop offset="1" stop-color="#e6e6e6"/>
    </radialGradient>
    <filter id="title-glow" x="-20%" y="-60%" width="140%" height="220%">
      <feGaussianBlur in="SourceAlpha" stdDeviation="5" result="blur"/>
      <feFlood flood-color="#2aa0ff" flood-opacity="0.9"/>
      <feComposite in2="blur" operator="in" result="glow"/>
      <feMerge>
        <feMergeNode in="glow"/>
        <feMergeNode in="SourceGraphic"/>
      </feMerge>
    </filter>
    <filter id="band-soft">
      <feGaussianBlur stdDeviation="3"/>
    </filter>
  </defs>

  <!-- disc body -->
  <circle class="disc-body" cx="600" cy="483" r="442" fill="var(--disc)"/>

  <!-- sweeping edge bands -->
  <g class="edge-bands" clip-path="url(#disc-edge)">
    <g filter="url(#band-soft)" fill="none">
      <path d="M560 20 C820 40 1010 230 1060 560" stroke="url(#band-top)" stroke-width="38" opacity="0.75"/>
      <path d="M600 10 C860 50 1040 250 1070 520" stroke="url(#band-top)" stroke-width="14" opacity="0.9"/>
      <path d="M140 520 C200 760 420 920 720 940" stroke="url(#band-bottom)" stroke-width="40" opacity="0.75"/>
      <path d="M150 590 C230 800 440 930 680 950" stroke="url(#band-bottom)" stroke-width="14" opacity="0.9"/>
    </g>
    <circle cx="600" cy="483" r="420" fill="none" stroke="var(--disc)" stroke-width="6" opacity="0.6"/>
  </g>

  <!-- centre hub -->
  <g class="disc-hub">
    <circle cx="600" cy="482" r="155" fill="var(--hub-outer)"/>
    <circle cx="600" cy="482" r="140" fill="none" stroke="var(--hub-ring)" stroke-width="6"/>
    <circle cx="600" cy="482" r="131" fill="url(#hub-shade)"/>
    <circle cx="600" cy="480" r="55" fill="var(--hub-inner)" stroke="#cfcfcf" stroke-width="1.5"/>
  </g>

  <!-- release title -->
  <g class="release-title" filter="url(#title-glow)" text-anchor="middle">
    <text class="disc-title" x="601" y="186">THE RADIANT HARBOR</text>
    <text class="disc-subtitle" x="601" y="212">ANTHOLOGY VOLUME 1</text>
  </g>

  <!-- record label name -->
  <g class="label-name" text-anchor="middle">
    <text class="label-number" x="600" y="838">371</text>
    <text class="label-word" x="604" y="866">RECORDS</text>
  </g>
</svg>
</body>
</html>
```